Falcon guarding business card

Looking for a business card for my security company

Target Market(s)

Security

Industry/Entity Type

Security

Contact Information for Business Card

Name - Dale Hutchins. Title - General manager - direct 318 642.9053 website www. falconguardingservices.example email - dale@ falconguardingservices.example

Requirements
Must have
• Logo attached

```html
<!DOCTYPE html>
<html lang="en">
<head>
<meta charset="utf-8">
<title>Falcon Guarding – Business Card</title>
<link rel="stylesheet" href="https://fonts.googleapis.com/css2?family=Arimo:wght@400;700&display=swap">
<style>
  :root {
    --backdrop: #e4e4e2;
    --card-white: #ffffff;
    --card-dark: #2c2c2c;
    --ink: #262626;
    --rule: #3a3a3a;
    --gold: #c9a24a;
    --emboss: #3d3d3d;
  }
  * { margin: 0; padding: 0; box-sizing: border-box; }
  html, body {
    width: 1200px; height: 801px; overflow: hidden;
    background: var(--backdrop);
    font-family: "Arimo", Arial, sans-serif;
    color: var(--ink);
  }
  .card {
    position: absolute;
    top: 245px;
    width: 540px; height: 310px;
    box-shadow: 0 6px 18px rgba(0,0,0,0.18);
  }
  .card-front { left: 40px; background: var(--card-white); border-bottom: 5px solid var(--gold); }
  .card-back { left: 620px; background: var(--card-dark); }

  .brand {
    position: absolute;
    display: flex; align-items: center; gap: 10px;
    font-weight: 700; text-transform: uppercase; letter-spacing: 1px;
    white-space: nowrap;
  }
  .brand-dot { width: 14px; height: 14px; border-radius: 50%; background: currentColor; }
  .card-front .brand { top: 64px; right: 70px; font-size: 30px; color: var(--ink); }
  .card-back .brand { top: 50%; left: 50%; transform: translate(-50%, -50%); font-size: 40px; color: var(--emboss); }

  .divider {
    position: absolute; left: 40px; right: 40px; top: 196px;
    height: 1px; background: var(--rule);
  }
  .person { position: absolute; left: 40px; top: 140px; }
  .person-name { font-size: 20px; font-weight: 700; text-transform: uppercase; letter-spacing: 0.5px; }
  .person-title { font-size: 16px; margin-top: 2px; }

  .contact { position: absolute; top: 212px; font-size: 15px; line-height: 24px; }
  .contact-left { left: 40px; }
  .contact-right { right: 40px; }
  .contact-line { display: flex; align-items: center; gap: 8px; }
  .contact-line svg { width: 13px; height: 13px; flex: none; }
</style>
</head>
<body>
  <section class="card card-front">
    <div class="brand"><span class="brand-dot"></span>Falcon guarding</div>
    <div class="person">
      <div class="person-name">Dale Hutchins</div>
      <div class="person-title">General manager</div>
    </div>
    <div class="divider"></div>
    <div class="contact contact-left">
      <div class="contact-line">
        <svg viewBox="0 0 16 16" aria-hidden="true"><path d="M3 1l3 3-2 2c1 2 3 4 5 5l2-2 3 3-2 3C6 15 1 10 1 3z" fill="var(--ink)"/></svg>
        <span>318 642.9053</span>
      </div>
      <div class="contact-line">
        <svg viewBox="0 0 16 16" aria-hidden="true"><rect x="1.5" y="3.5" width="13" height="9" fill="none" stroke="var(--ink)" stroke-width="1.5"/><path d="M1.5 3.5l6.5 5 6.5-5" fill="none" stroke="var(--ink)" stroke-width="1.5"/></svg>
        <span>dale@falconguardingservices.example</span>
      </div>
    </div>
    <div class="contact contact-right">
      <div class="contact-line">
        <svg viewBox="0 0 16 16" aria-hidden="true"><circle cx="8" cy="8" r="6.5" fill="none" stroke="var(--ink)" stroke-width="1.4"/><path d="M1.5 8h13M8 1.5c-3 3-3 10 0 13M8 1.5c3 3 3 10 0 13" fill="none" stroke="var(--ink)" stroke-width="1.2"/></svg>
        <span>www.falconguardingservices.example</span>
      </div>
    </div>
  </section>

  <section class="card card-back">
    <div class="brand"><span class="brand-dot"></span>Falcon guarding</div>
  </section>
</body>
</html>
```